Webbanner-Design für Tanzschule
Zielgruppe
Wir sind eine Tanzschule und benötigen einen werbebanner.
Aufgabenstellung
Hierfür benötigen wir eine Banner (Haeder): https://www.tanzkreisnord.de/page/3/
Es soll enthalten sein:
Logo: Ritmo del Alba
Angebot: Salsa, Bachata, Kizomba, Zouk, Lady- & Menstyle
Einstiegsmöglichkeiten Jederzeit
Gratis Schnupperstunde - es soll zum Klick animieren
Es soll dich zum Tanzen einladen und professionell wirken.
Die Bilder sind nur eine Idee.
https://www.ritmo-del-alba.de/
It should contain:
Offer: Salsa, Bachata, Kizomba, Zouk, Lady- & Menstyle
Join the courses every month
Free trial lesson - it should encourage you to click
It should invite you to dance and look professional!
The pictures are just an idea!

```html
<!DOCTYPE html>
<html lang="de">
<head>
<meta charset="utf-8">
<title>Ritmo del Alba – Tanzschule Banner</title>
<link href="https://fonts.googleapis.com/css2?family=Red+Hat+Display:ital,wght@0,400;0,700;1,700;1,800&display=swap" rel="stylesheet">
<style>
  :root {
    --stage: #e9e9e9;
    --magenta: #b01a66;
    --yellow: #ffdc00;
    --white: #ffffff;
    --photo-dark: #2a1712;
    --photo-mid: #6b3a26;
    --photo-warm: #b0653d;
    --photo-light: #d9b7a2;
  }
  * { box-sizing: border-box; margin: 0; padding: 0; }
  html, body {
    width: 1200px; height: 529px; overflow: hidden;
    background: var(--stage);
    font-family: "Red Hat Display", "Helvetica Neue", Arial, sans-serif;
  }
  .banner {
    position: absolute; left: 0; top: 54px;
    width: 1200px; height: 421px; overflow: hidden;
  }
  .banner__photo {
    position: absolute; inset: 0;
    background:
      radial-gradient(ellipse 220px 300px at 700px 230px, rgba(120,70,50,0.55), transparent 70%),
      radial-gradient(ellipse 300px 260px at 120px 330px, rgba(217,183,162,0.55), transparent 70%),
      radial-gradient(ellipse 200px 300px at 1160px 220px, rgba(176,101,61,0.7), transparent 70%),
      linear-gradient(90deg, var(--photo-mid) 0%, var(--photo-dark) 35%, var(--photo-mid) 60%, var(--photo-dark) 85%, var(--photo-warm) 100%);
  }
  .brand {
    position: absolute; left: 34px; top: 52px;
    display: flex; align-items: center; gap: 14px;
  }
  .brand__name {
    font-weight: 700; font-size: 40px; color: var(--white); letter-spacing: 0.5px;
  }
  .brand__mark {
    width: 46px; height: 46px; border-radius: 50%; background: var(--magenta);
  }
  .brand__tagline {
    position: absolute; left: 100px; top: 110px;
    font-weight: 400; font-size: 15px; color: var(--white); opacity: .9;
  }
  .entry {
    position: absolute; left: 28px; width: 320px; top: 210px;
    text-align: center; color: var(--yellow);
    font-style: italic; font-weight: 800; font-size: 28px; line-height: 35px;
  }
  .offer {
    position: absolute; right: 54px; top: 38px; list-style: none;
  }
  .offer__item {
    display: flex; align-items: center; justify-content: flex-end;
    height: 46.5px; gap: 20px;
    color: var(--white); font-style: italic; font-weight: 800; font-size: 28px;
  }
  .offer__dot {
    width: 35px; height: 35px; border-radius: 50%; flex: none;
  }
  .offer__dot--yellow { background: var(--yellow); }
  .offer__dot--magenta { background: var(--magenta); }
  .offer__dot--none { visibility: hidden; }
  .cta {
    position: absolute; left: 801px; top: 340px;
    width: 365px; height: 59px;
    background: var(--magenta);
    display: flex; align-items: center; justify-content: center; gap: 7px;
    font-style: italic; font-weight: 800; font-size: 28px;
    color: var(--white); text-decoration: none;
  }
  .cta__free { color: var(--yellow); }
</style>
</head>
<body>
  <section class="banner">
    <div class="banner__photo" role="img" aria-label="Tanzpaar in enger Umarmung vor unscharfem, warm beleuchtetem Tanzsaal"></div>

    <div class="brand">
      <span class="brand__name">Ritmo del Alba</span>
      <span class="brand__mark"></span>
    </div>
    <p class="brand__tagline">Salsa · Bachata · Kizomba</p>

    <p class="entry">Einstiegsmöglichkeiten<br>Jederzeit</p>

    <ul class="offer">
      <li class="offer__item">Salsa <span class="offer__dot offer__dot--yellow"></span></li>
      <li class="offer__item">Bachata <span class="offer__dot offer__dot--magenta"></span></li>
      <li class="offer__item">Kizomba <span class="offer__dot offer__dot--yellow"></span></li>
      <li class="offer__item">Zouk Lady- <span class="offer__dot offer__dot--magenta"></span></li>
      <li class="offer__item">&amp; Menstyle <span class="offer__dot offer__dot--none"></span></li>
    </ul>

    <a class="cta" href="#"><span class="cta__free">GRATIS</span> Schnupperstunde</a>
  </section>
</body>
</html>
```